Willowbend Pharmacy Business Cards

I need a business card design and or template. Needs to convey a softer feel along with health and wellness. Please see attached logo and color scheme.

Industry/Entity Type

Pharmacy

Colors

Designer to choose colors to be used in the design.

Requirements
Must have
• I've added a second NEW colored logo I think I am going to go with the blue green logo.
• Needs to have the colors and feel of the logo attached.
• Darrel Quimby
• Pharmacy Manager
• willowbendpharmacy.example

```html
<!DOCTYPE html>
<html lang="en">
<head>
<meta charset="utf-8">
<title>Willowbend Pharmacy Business Cards</title>
<link rel="stylesheet" href="https://fonts.googleapis.com/css2?family=Jost:wght@400;500;600;700&display=swap">
<style>
  :root {
    --backdrop: #2b2b2b;
    --brand-blue: #3d9fd1;
    --brand-blue-light: #4aaedd;
    --brand-green: #93bb3c;
    --card-white: #f4f4f4;
    --ink-grey: #5b5f63;
    --text-white: #ffffff;
  }
  * { margin: 0; padding: 0; box-sizing: border-box; }
  html, body {
    width: 1200px;
    height: 960px;
    overflow: hidden;
    background: var(--backdrop);
    font-family: "Jost", "Futura", sans-serif;
  }
  .canvas { position: relative; width: 1200px; height: 960px; }

  .card {
    position: absolute;
    left: 320px;
    width: 600px;
    height: 345px;
    overflow: hidden;
  }
  .card-front { top: 100px; }
  .card-back { top: 491px; background: var(--brand-green); }

  .front-shapes { position: absolute; inset: 0; width: 600px; height: 345px; }

  .contact-block {
    position: absolute;
    left: 27px;
    top: 27px;
    color: var(--text-white);
  }
  .holder-name { font-size: 21px; font-weight: 600; line-height: 1.1; }
  .holder-title { font-size: 15.5px; font-weight: 700; line-height: 1.3; margin-bottom: 10px; }
  .contact-list { list-style: none; }
  .contact-item {
    display: flex;
    align-items: center;
    gap: 8px;
    font-size: 14.5px;
    font-weight: 400;
    line-height: 20px;
  }
  .contact-icon { width: 13px; height: 13px; flex: none; fill: var(--text-white); }

  .brand-front {
    position: absolute;
    left: 295px;
    top: 258px;
    display: flex;
    align-items: center;
    gap: 12px;
    color: var(--ink-grey);
    font-size: 24px;
    font-weight: 500;
  }
  .brand-dot {
    width: 40px; height: 40px; border-radius: 50%;
    background: var(--brand-blue);
  }

  .brand-back {
    position: absolute;
    left: 0; right: 0;
    top: 130px;
    display: flex;
    justify-content: center;
    align-items: center;
    gap: 16px;
    color: var(--text-white);
    font-size: 34px;
    font-weight: 500;
  }
  .brand-back .brand-dot { width: 64px; height: 64px; background: var(--text-white); }

  .back-web {
    position: absolute;
    left: 0; right: 0;
    top: 300px;
    text-align: center;
    color: var(--text-white);
    font-size: 14px;
    letter-spacing: 3.2px;
  }
</style>
</head>
<body>
<main class="canvas">

  <section class="card card-front">
    <svg class="front-shapes" viewBox="0 0 600 345" aria-hidden="true">
      <defs>
        <linearGradient id="blueField" x1="0" y1="0" x2="0" y2="1">
          <stop offset="0" stop-color="var(--brand-blue)"/>
          <stop offset="1" stop-color="var(--brand-blue-light)"/>
        </linearGradient>
      </defs>
      <rect width="600" height="345" fill="url(#blueField)"/>
      <path d="M585 0 C390 40 240 190 175 345 L600 345 L600 0 Z" fill="var(--brand-green)"/>
      <path d="M600 6 C400 50 255 200 189 345 L600 345 Z" fill="var(--card-white)"/>
    </svg>

    <div class="contact-block">
      <h1 class="holder-name">Darrel Quimby</h1>
      <p class="holder-title">Pharmacy Manager</p>
      <ul class="contact-list">
        <li class="contact-item">
          <svg class="contact-icon" viewBox="0 0 16 16"><path d="M1 6 C1 2 15 2 15 6 L15 8 L11 8 L11 6 L5 6 L5 8 L1 8 Z M3 9 L13 9 L14 15 L2 15 Z"/></svg>
          555 014 2873
        </li>
        <li class="contact-item">
          <svg class="contact-icon" viewBox="0 0 16 16"><path d="M4 0 H12 V16 H4 Z M5.5 2 V12 H10.5 V2 Z"/></svg>
          555 019 4406
        </li>
        <li class="contact-item">
          <svg class="contact-icon" viewBox="0 0 16 16"><path d="M1 3 H15 V4 L8 9 L1 4 Z M1 6 L8 11 L15 6 V13 H1 Z"/></svg>
          darrel@willowbendpharmacy.example
        </li>
        <li class="contact-item">
          <svg class="contact-icon" viewBox="0 0 16 16"><circle cx="8" cy="8" r="7"/><path d="M4 5 C6 4 7 7 5 9 C7 10 6 13 8 14 C6 14 3 12 3 8 Z M9 3 C11 4 12 6 10 7 C12 9 13 8 14 9 C13 5 11 3 9 3 Z" fill="var(--brand-blue)"/></svg>
          willowbendpharmacy.example
        </li>
      </ul>
    </div>

    <div class="brand-front">
      <span class="brand-dot"></span>
      <span class="brand-name">Willowbend Pharmacy</span>
    </div>
  </section>

  <section class="card card-back">
    <div class="brand-back">
      <span class="brand-dot"></span>
      <span class="brand-name">Willowbend Pharmacy</span>
    </div>
    <p class="back-web">www.willowbendpharmacy.example</p>
  </section>

</main>
</body>
</html>
```